Law Firm Needs Brochure Redesign Using New Logo

We are a personal injury law firm that does auto injuries and other personal injury cases. We want a new brochure that has our updated logo and information. Instead of gold and black, we want more navy, as matches the new logo. The Auto Liability portion should read: "(required by the state of Arizona in the amounts of $25,000 per person / $50,000 per accident, but a higher amount may be best )." The other information can remain the same. We'd like the brochure to keep the same professional tone as the previous brochure.
Our website is https://www.marbrenlegal.com/.

```html
<!DOCTYPE html>
<html lang="en">
<head>
<meta charset="utf-8">
<title>Marbren Legal – Top 10 Tips to Avoid a Crash</title>
<link href="https://fonts.googleapis.com/css2?family=Inter:wght@400;600;700&family=Montserrat:wght@600;700&display=swap" rel="stylesheet">
<style>
  :root{
    --navy:#0e2346;
    --ink:#101828;
    --black:#1b1b1c;
    --teal:#27505c;
    --steel:#36679a;
    --white:#ffffff;
  }
  *{box-sizing:border-box;margin:0;padding:0}
  html,body{width:1200px;height:848px;overflow:hidden;background:var(--white)}
  .brochure{position:relative;width:1200px;height:848px;overflow:hidden;font-family:"Inter",sans-serif;color:var(--ink)}
  .shapes{position:absolute;inset:0}
  .abs{position:absolute}
  .title-box{left:32px;top:30px;width:343px;height:87px;background:var(--navy);color:var(--white);
    font-family:"Montserrat",sans-serif;font-weight:600;font-size:21px;line-height:24px;text-align:center;
    display:flex;align-items:center;justify-content:center;letter-spacing:.3px}
  .tips{left:29px;top:199px;width:310px;list-style:none}
  .tip{position:absolute;left:0;width:310px;font-size:13.1px;line-height:17.2px}
  .tip b{font-weight:700}
  .tip .sub{display:block;margin-top:3px}
  .tip.wide{width:335px}
  .photo-coverage{left:400px;top:0;width:402px;height:290px;
    background:linear-gradient(160deg,#e9e4d0 0%,#c9c6ad 35%,#8d8f66 60%,#5e6440 85%,#3f3f35 100%);
    clip-path:polygon(0 0,100% 0,100% 72%,50% 100%,0 72%)}
  .coverage-head{left:415px;top:38px;font-weight:700;font-size:17px;color:#13202f;letter-spacing:.2px}
  .coverage-intro{left:416px;top:67px;width:230px;font-size:14.2px;line-height:17.3px;color:#13202f}
  .cover-list{left:422px;width:350px}
  .cover-item{position:absolute;left:0;width:350px}
  .cover-item h3{font-weight:600;font-size:17.4px;line-height:21px;margin-left:24px;color:var(--ink)}
  .cover-item p{font-size:13.2px;line-height:15.7px;margin:6px 0 0 24px}
  .cover-item svg{position:absolute;left:0;top:4px}
  .photo-safety{left:828px;top:33px;width:344px;height:332px;
    background:linear-gradient(135deg,#5d7ea8 0%,#3a5a86 40%,#223b62 70%,#1c2a44 100%);
    clip-path:polygon(0 0,100% 0,100% 67.5%,0 100%)}
  .photo-safety-tint{left:828px;top:33px;width:344px;height:332px;background:linear-gradient(90deg,transparent 55%,rgba(210,95,60,.45) 100%);
    clip-path:polygon(0 0,100% 0,100% 30%,0 30%)}
  .safety-title{left:848px;top:172px;color:var(--white);font-family:"Montserrat",sans-serif;font-weight:700;font-size:36px;line-height:39px;letter-spacing:.2px}
  .behave{left:855px;width:285px}
  .behave h3{font-weight:600;font-size:17px;line-height:20px}
  .behave p{font-size:13.2px;line-height:15.6px;margin-top:5px}
  .behave .strong{font-weight:700;font-size:11.6px;line-height:14px;margin-top:8px}
  .brand{left:968px;top:780px;display:flex;align-items:center;gap:10px;color:var(--white)}
  .brand-mark{width:30px;height:30px;border-radius:50%;background:var(--white)}
  .brand-name{font-family:"Inter",sans-serif;font-weight:700;font-size:19px;line-height:20px;letter-spacing:.5px}
  .brand-name small{display:block;font-weight:700;font-size:7.5px;letter-spacing:3.4px;margin-top:3px}
</style>
</head>
<body>
<main class="brochure">
  <svg class="shapes" width="1200" height="848" viewBox="0 0 1200 848" aria-hidden="true">
    <polygon points="0,0 1200,0 1200,70 1172,100 1172,33 828,33 828,365 735,260 468,256 0,85" fill="var(--black)"/>
    <polygon points="0,60 400,225 468,256 0,85" fill="var(--teal)"/>
    <polygon points="735,260 802,205 802,225 752,245" fill="var(--teal)"/>
    <polygon points="1172,80 1200,70 1200,92 1172,100" fill="var(--teal)"/>
    <polygon points="835,672 1179,562 1179,848 835,848" fill="var(--navy)"/>
    <polygon points="971,660 1200,584 1200,604 971,688" fill="var(--steel)"/>
    <polygon points="1017,668 1200,604 1200,632 1017,690" fill="var(--black)"/>
    <polygon points="670,848 892,770 892,798 730,848" fill="var(--steel)"/>
  </svg>

  <div class="abs photo-coverage" role="img" aria-label="Photo of a woman in a sun hat sitting on the open trunk of a silver hatchback beside a hillside road"></div>
  <div class="abs photo-safety" role="img" aria-label="Photo of a driver in a denim jacket fastening a seat belt"></div>
  <div class="abs photo-safety-tint" aria-hidden="true"></div>

  <svg class="abs" style="left:558px;top:262px" width="92" height="92" viewBox="0 0 92 92" aria-hidden="true">
    <rect x="16" y="16" width="60" height="60" transform="rotate(45 46 46)" fill="var(--navy)" stroke="#2c4f7a" stroke-width="2"/>
    <path d="M46 33v26M36 50l10 10 10-10" fill="none" stroke="#fff" stroke-width="2"/>
  </svg>

  <h1 class="abs title-box">TOP 10 TIPS TO AVOID A<br>CRASH</h1>

  <svg class="abs" style="left:0;top:0" width="24" height="848" viewBox="0 0 24 848" aria-hidden="true">
    <g fill="var(--navy)">
      <polygon points="0,188 18,207 0,226"/><polygon points="0,278 18,297 0,316"/><polygon points="0,336 18,355 0,374"/>
      <polygon points="0,412 18,431 0,450"/><polygon points="0,484 18,503 0,522"/><polygon points="0,572 18,591 0,610"/>
      <polygon points="0,630 18,649 0,668"/><polygon points="0,720 18,739 0,758"/><polygon points="0,774 18,793 0,812"/>
    </g>
    <g fill="none" stroke="#fff" stroke-width="1.5">
      <path d="M4,201l6,6-6,6"/><path d="M4,291l6,6-6,6"/><path d="M4,349l6,6-6,6"/><path d="M4,425l6,6-6,6"/>
      <path d="M4,497l6,6-6,6"/><path d="M4,585l6,6-6,6"/><path d="M4,643l6,6-6,6"/><path d="M4,733l6,6-6,6"/><path d="M4,787l6,6-6,6"/>
    </g>
  </svg>

  <ol class="abs tips">
    <li class="tip" style="top:0"><b>Anyone making a left turn must wait for all oncoming traffic to clear before proceeding.</b><span class="sub">Yes, even if the light has turned yellow. Wait to be sure that all traffic has stopped.</span></li>
    <li class="tip" style="top:90px"><b>When your light turns green,</b> check to be sure that no vehicles are entering the intersection late.</li>
    <li class="tip" style="top:147px"><b>Allow plenty of room between you and the car in front of you.</b> Traffic can stop in an instant, even if you can’t see anything ahead.</li>
    <li class="tip" style="top:223px"><b>Avoid being distracted.</b> Teenagers are especially susceptible to losing focus if there are too many friends in the car.</li>
    <li class="tip" style="top:294px"><b>Keep the volume of your radio down and never wear headphones.</b> Cars are very soundproof these days, but you need to be able to hear an ambulance or police siren.</li>
    <li class="tip" style="top:383px"><b>Be especially careful on the weekends<br>and early morning hours.</b></li>
    <li class="tip wide" style="top:441px"><b>Dont speed.</b> Speed is a factor in most crashes.<br>Street lights are timed and the freeway has<br>traffic. It’s likely you won’t get there much faster<br>even if you do speed.</li>
    <li class="tip" style="top:531px"><b>Don’t drink and drive.</b> Many cab companies offer a free service to get you home safe.</li>
    <li class="tip wide" style="top:585px"><b>Use your turn signals.</b> This gives an early warning<br>to vehicles you may not be able to see.</li>
  </ol>

  <h2 class="abs coverage-head">HAVE THE RIGHT COVERAGE</h2>
  <p class="abs coverage-intro">Many people don’t know about the different kinds of insurance available. In addition to health insurance, we suggest:</p>

  <div class="abs cover-list" style="top:362px">
    <div class="cover-item" style="top:0">
      <svg width="10" height="16" viewBox="0 0 10 16"><path d="M2 2l6 6-6 6" fill="none" stroke="#111" stroke-width="1.6"/></svg>
      <h3>Auto Liability</h3>
      <p>Required by the state of Arizona in the amounts of $25,000 per person / $50,000 per accident, but a higher amount may be best.</p>
    </div>
    <div class="cover-item" style="top:115px">
      <svg width="10" height="16" viewBox="0 0 10 16"><path d="M2 2l6 6-6 6" fill="none" stroke="#111" stroke-width="1.6"/></svg>
      <h3>Uninsured or Underinsured<br>Motorist Coverage</h3>
      <p style="margin-top:10px">This protects YOU when the other driver doesn’t have insurance or not enough.</p>
    </div>
    <div class="cover-item" style="top:239px">
      <svg width="10" height="16" viewBox="0 0 10 16"><path d="M2 2l6 6-6 6" fill="none" stroke="#111" stroke-width="1.6"/></svg>
      <h3>Medical Payments Coverage</h3>
      <p>Up to $5,000 in coverage will be paid out to you no matter who is at fault in an accident and does not need to be reimbursed.</p>
    </div>
    <div class="cover-item" style="top:363px">
      <svg width="10" height="16" viewBox="0 0 10 16"><path d="M2 2l6 6-6 6" fill="none" stroke="#111" stroke-width="1.6"/></svg>
      <h3>Homeowners / Renters Insurance</h3>
      <p>. Protects you in case of injuries on your property as well as damage to your home from covered events.</p>
    </div>
  </div>

  <h2 class="abs safety-title">MODEL<br>SAFE BEHAVIOR</h2>

  <section class="abs behave" style="top:378px">
    <h3>Always buckle up.</h3>
    <p>Always put your children in car seats/boosters that are rated for their height and weight.</p>
  </section>
  <section class="abs behave" style="top:480px">
    <h3>Never Text While Driving.</h3>
    <p>Studies have shown that texting while driving is as dangerous as driving intoxicated.</p>
    <p class="strong">Show your children that no text is more important than your safety. It can wait.</p>
  </section>

  <div class="abs brand">
    <span class="brand-mark" aria-hidden="true"></span>
    <span class="brand-name">MARBREN LEGAL<small>INJURY LAWYERS</small></span>
  </div>
</main>
</body>
</html>
```